Speisekarten
Zielgruppe
we run a restaurant and our target groups are families and business people
Aufgabenstellung
The menu consists of a black folder with 8 DIN A4 slots which have a 2 cm border on all sides. The card should be discreet, classy and easy to read without any kind of complicated fonts or pictures. we would like to see creative designs regarding our recommendation at the end of page 3.

```html
<!DOCTYPE html>
<html lang="de">
<head>
<meta charset="utf-8">
<title>Soraya – Speisekarte</title>
<link href="https://fonts.googleapis.com/css2?family=Dosis:wght@600;700&family=Montserrat:wght@400;500;600;700&family=Dancing+Script:wght@600&display=swap" rel="stylesheet">
<style>
  :root{
    --backdrop:#dcdcdc;
    --paper:#ffffff;
    --ink:#1e1e1e;
    --gold:#6f5a2b;
    --gold-soft:#8d6c2c;
    --veg:#2f9467;
    --rule:#3a3a3a;
  }
  *{box-sizing:border-box;margin:0;padding:0}
  html,body{width:1200px;height:560px;overflow:hidden}
  body{background:var(--backdrop);font-family:"Montserrat",sans-serif;color:var(--ink);position:relative}

  .page{position:absolute;top:14px;height:528px;background:var(--paper);box-shadow:3px 4px 6px rgba(0,0,0,.28);overflow:hidden}
  .page--aperitif{left:17px;width:375px}
  .page--starters{left:409px;width:375px}
  .page--mains{left:802px;width:376px}

  .brand{position:absolute;left:0;right:0;top:52px;text-align:center}
  .brand__dot{display:block;width:18px;height:18px;border-radius:50%;background:var(--gold);margin:0 auto 10px}
  .brand__name{font-family:"Dosis",sans-serif;font-weight:700;font-size:38px;letter-spacing:3px;color:var(--gold)}

  .heading{position:absolute;display:flex;align-items:center;gap:8px;font-family:"Dosis",sans-serif;font-weight:700;font-size:14px;letter-spacing:1.2px;color:var(--ink);white-space:nowrap;line-height:1}
  .heading__rule{flex:1;height:3px;border-top:1px solid var(--rule);border-bottom:1px solid var(--gold)}
  .heading__en,.heading__slash{color:var(--gold)}
  .heading__slash{font-weight:600;margin:0 1px}

  .drinks{position:absolute;left:50px;width:272px;top:217px;list-style:none}
  .drink{display:flex;align-items:baseline;font-size:7.4px;height:16.3px}
  .drink b{font-weight:600}
  .lead{flex:1;border-bottom:1px dotted #555;margin:0 2px 1.5px;min-width:6px}
  .lead--short{flex:0 0 16px}

  .cols{position:absolute;display:grid;grid-template-columns:1fr 1fr;column-gap:22px;align-items:start}
  .col{display:flex;flex-direction:column}
  .item{margin-bottom:7.5px}
  .item__row{display:flex;align-items:baseline;font-size:6.9px;line-height:1.2;font-weight:600;white-space:nowrap}
  .item__price{font-weight:500}
  .tag{font-family:"Dancing Script",cursive;font-weight:600;font-size:6.4px;color:var(--veg);margin-left:2px}
  .de,.en{font-size:4.3px;line-height:1.5;font-weight:400}
  .de{margin-top:1.5px}
  .en{color:var(--gold-soft)}

  .starters{left:50px;right:49px;top:64px}
  .salads{left:50px;right:49px;top:350px}
  .dressing{position:absolute;left:0;right:0;top:462px;text-align:center;font-size:5px;color:var(--gold-soft)}
  .dressing b{color:var(--ink);font-weight:600;margin-right:3px}

  .intro{position:absolute;left:30px;right:30px;text-align:center;font-size:5.1px;line-height:1.3}
  .intro p+p{margin-top:5px}
  .page--mains .cols{left:46px;right:46px;column-gap:18px}
  .page--mains .item{margin-bottom:3px}
  .page--mains .de,.page--mains .en{font-size:4px;line-height:1.4;letter-spacing:-.05px}
  .page--mains .de{margin-top:1px}
  .grill{top:88px}
  .braised{top:236px}
  .rice{top:374px}
  .recommend{position:absolute;left:20px;right:20px;top:498px;text-align:center;font-size:4.9px;line-height:1.3}
  .en-line{color:var(--gold-soft)}
</style>
</head>
<body>

<section class="page page--aperitif">
  <div class="brand"><span class="brand__dot"></span><span class="brand__name">SORAYA</span></div>

  <h2 class="heading" style="left:50px;right:53px;top:175px"><span class="heading__rule"></span><span class="heading__en">Aperitif</span><span class="heading__rule"></span></h2>

  <ul class="drinks">
    <li class="drink"><b>LUMIÈRE WILD BERRY</b><span class="lead"></span>0,2L | 9,00</li>
    <li class="drink"><b>HUGO</b><span class="lead"></span>0,2L | 8,50</li>
    <li class="drink"><b>ARANCIO SPRITZ</b><span class="lead"></span>0,2L | 8,50</li>
    <li class="drink"><b>SEKT ARANCIO</b><span class="lead"></span>0,1L | 8,00</li>
    <li class="drink"><b>ROSSANO ORANGE</b><span class="lead"></span>0,2L | 7,50</li>
    <li class="drink"><b>ROSSANO SODA</b><span class="lead"></span>0,2L | 7,00</li>
    <li class="drink"><b>MARTELLO BIANCO</b>&nbsp;| Rosso | extra dry<span class="lead"></span>5CL | 7,00</li>
    <li class="drink"><b>RIESLING SEKT</b>&nbsp;trocken<span class="lead"></span>0,75L | 30,00</li>
    <li class="drink"><b>RIESLING SEKT</b>&nbsp;trocken<span class="lead"></span>0,1L | 8,00</li>
    <li class="drink"><b>VON EICHEN RIESLING</b>&nbsp;Brut 2017<span class="lead"></span>0,75L | 45,90</li>
    <li class="drink"><b>DOM VALMONT</b>&nbsp;vintage<span class="lead"></span>0,75 L | 295,00</li>
    <li class="drink"><b>MAISON CLAIRVAL</b>&nbsp;Brut<span class="lead"></span>0,2L | 25,00<span class="lead lead--short"></span>0,75L | 95,00</li>
    <li class="drink"><b>MAISON CLAIRVAL</b>&nbsp;Rose<span class="lead"></span>0,2L | 28,00<span class="lead lead--short"></span>0,75L | 125,00</li>
    <li class="drink"><b>BRUNEL &amp; LAVAUX</b>&nbsp;crémant saphir brut vintage loire<span class="lead"></span>0,75L | 45,00</li>
    <li class="drink"><b>BRUNEL &amp; LAVAUX</b>&nbsp;crémant rosé brut excellence loire<span class="lead"></span>0,75L | 45,00</li>
  </ul>
</section>

<section class="page page--starters">
  <h2 class="heading" style="left:50px;right:49px;top:31px"><span class="heading__rule"></span>Vorspeisen<span class="heading__slash">//</span><span class="heading__en">Starters</span><span class="heading__rule"></span></h2>

  <div class="cols starters">
    <div class="col">
      <div class="item"><div class="item__row">KASHKE-BADEMJAN<span class="tag">vegetarisch</span><span class="lead"></span><span class="item__price">11,50</span></div><p class="de">Gebratene und gehackte Auberginen mit einem Hauch Knoblauch, Pfefferminzöl, Röstzwiebeln und Joghurt-Sauce (Kashk)</p><p class="en">Chopped and fried aubergines with a touch of garlic, peppermint, roasted onions and yoghurt sauce (kashk)</p></div>
      <div class="item"><div class="item__row">MIRZA GHASSEMI<span class="tag">vegetarisch</span><span class="lead"></span><span class="item__price">11,50</span></div><p class="de">Gegrillte und gehackte Auberginen mit einem Hauch Knoblauch, Tomaten und Ei</p><p class="en">Chopped and grilled aubergines with a touch of garlic, tomatoes and eggs</p></div>
      <div class="item"><div class="item__row">SCHAFSKÄSE<span class="lead"></span><span class="item__price">3,00</span></div><p class="en">Feta cheese</p></div>
      <div class="item"><div class="item__row">HUMMUS<span class="tag">vegan</span><span class="lead"></span><span class="item__price">6,50</span></div><p class="de">Pürierte Kichererbsen mit einem Hauch Knoblauch und Sesam-Mus</p><p class="en">Pureed chickpeas, sesame nutmeg and a touch of garlic</p></div>
      <div class="item"><div class="item__row">ZEYTUN PARVARDE<span class="tag">vegan</span><span class="lead"></span><span class="item__price">6,50</span></div><p class="de">Grüne Oliven eingelegt in einer Kräuter-Granatapfel-Sauce mit Walnüssen und einem Hauch Knoblauch</p><p class="en">Green olives marinated in an herb-pomegranate-sauce with walnuts and a touch of garlic</p></div>
      <div class="item"><div class="item__row">ZEYTUN<span class="tag">vegan</span><span class="lead"></span><span class="item__price">4,00</span></div><p class="de">Oliven</p><p class="en">Olives</p></div>
    </div>
    <div class="col">
      <div class="item"><div class="item__row">BORANI BADEMJAN<span class="tag">vegetarisch</span><span class="lead"></span><span class="item__price">4,50</span></div><p class="de">Auberginen-Joghurt mit Knoblauch</p><p class="en">Aubergine-yoghurt with garlic</p></div>
      <div class="item"><div class="item__row">BORANI<span class="tag">vegetarisch</span><span class="lead"></span><span class="item__price">4,50</span></div><p class="de">Spinat-Joghurt mit einem Hauch Knoblauch</p><p class="en">Spinach-yoghurt with a touch of garlic</p></div>
      <div class="item"><div class="item__row">DOLMEH<span class="tag">vegetarisch</span><span class="lead"></span><span class="item__price">5,00</span></div><p class="de">Gefüllte Weinblätter (vegetarisch)</p><p class="en">Stuffed vine leaves (vegetarian)</p></div>
      <div class="item"><div class="item__row">KRÄUTERTELLER<span class="tag">vegetarisch</span><span class="lead"></span><span class="item__price">4,00</span></div><p class="de">Basilikum, Minze, Estragon, Petersilie, Schafskäse, Radieschen und Zwiebel</p><p class="en">Basil, peppermint, tarragon, parsley, feta cheese, radishes and onion</p></div>
      <div class="item"><div class="item__row">GEMISCHTER VORSPEISENTELLER</div><div class="item__row">(ab 2 Personen) pro Person<span class="lead"></span><span class="item__price">12,50</span></div><p class="en">Mixed appetizer plate (from 2 persons) per person</p></div>
      <div class="item"><div class="item__row">SUPPE DJO<span class="lead"></span><span class="item__price">7,00</span></div><p class="de">Perlgraupensuppe</p><p class="en">Barley soup</p></div>
      <div class="item"><div class="item__row">SUPPE ADAS<span class="tag">vegan</span><span class="lead"></span><span class="item__price">7,00</span></div><p class="de">Linsen suppe</p><p class="en">Lentil soup</p></div>
      <div class="item"><div class="item__row">ASHE RESHTEH<span class="tag">vegetarisch</span><span class="lead"></span><span class="item__price">8,00</span></div><p class="de">Nudelsuppe mit Kräutern, Kichererbse, Bohnen, Röstzwiebel und Kashk</p><p class="en">Noodle soup with herbs, chickpeas, beans, roasted onions</p></div>
    </div>
  </div>

  <h2 class="heading" style="left:52px;right:50px;top:317px"><span class="heading__rule"></span>Salate<span class="heading__slash">//</span><span class="heading__en">Salads</span><span class="heading__rule"></span></h2>

  <div class="cols salads">
    <div class="col">
      <div class="item"><div class="item__row">GEMISCHTER SALAT<span class="tag">vegetarisch</span><span class="lead"></span><span class="item__price">10,90</span></div><p class="de">Salat, Gurken, Tomaten, Oliven, Schafskäse und Mais</p><p class="en">Salad with lettuce, cucumbers, tomatoes, olives, feta cheese and maize</p></div>
      <div class="item"><div class="item__row">SALAT SHIRAZI<span class="tag">vegan</span><span class="lead"></span><span class="item__price">5,00</span></div><p class="de">Fein zerkleinerte Gurken, Tomaten und Zwiebeln, dazu Zitronensaft-Olivenöl-Dressing</p><p class="en">Salad with finely chopped cucumbers, tomatoes, onions with lemon juice and olive oil dressing</p></div>
      <div class="item"><div class="item__row">GRÜNER SALAT<span class="tag">vegetarisch</span><span class="lead"></span><span class="item__price">5,90</span></div><p class="de">Salat, Gurken und Tomaten</p><p class="en">Salad with lettuce, cucumbers and tomatoes</p></div>
    </div>
    <div class="col">
      <div class="item"><div class="item__row">SORAYA SALAT<span class="lead"></span><span class="item__price">19,00</span></div><p class="de">Salat mit gegrillte Maishähnchenbrust, Gurken, Tomaten, Oliven, Schafskäse und Mais</p><p class="en">One skewer of corn chicken breast pieces with Salad Olives, Cucumber, Tomato, Sheep cheese &amp; Corn</p></div>
      <div class="item"><div class="item__row">SALAT OLVIEH<span class="lead"></span><span class="item__price">7,00</span></div><p class="de">Pürierter Kartoffelsalat mit Maishähnchenbrust, Eiern und Salzgurken</p><p class="en">Mashed potato salad with corn chicken breast, eggs and pickled cucumbers</p></div>
    </div>
  </div>

  <p class="dressing"><b>DRESSING</b>Honig-Senf Dressing • French Dressing • Essig und Öl</p>
</section>

<section class="page page--mains">
  <h2 class="heading" style="left:52px;right:52px;top:31px"><span class="heading__rule"></span>Grillgerichte<span class="heading__slash">//</span><span class="heading__en">grill dishes</span><span class="heading__rule"></span></h2>
  <div class="intro" style="top:50px">
    <p>Alle Grillgerichte werden mit Safran verfeinertem Basmatireis und Grilltomate Serviert<br><span class="en-line">All grill dishes are served with saffron rice and grilled tomato</span></p>
    <p>Alle Gerichte können auf Wunsch gegen 1,00 € Aufpreis mit Baghali- oder Sereshk-Polo serviert werden<br><span class="en-line">All dishes are available also with Baghali- or Sereshk-Polo. Extra charge 1,00 €</span></p>
  </div>

  <div class="cols grill">
    <div class="col">
      <div class="item"><div class="item__row">SOLTANI<span class="lead"></span><span class="item__price">28,00</span></div><p class="de">Ein Spieß aus flach geklopftem Lammrücken- und ein Lammhackfleisch-Spieß</p><p class="en">One skewer of lamb rack and one of lamb minced meat</p></div>
      <div class="item"><div class="item__row">KUBIDEH<span class="lead"></span><span class="item__price">18,00</span></div><p class="de">Zwei Lammhackfleischspieße</p><p class="en">Two Skewers of lamb minced meat</p></div>
      <div class="item"><div class="item__row">DJUDJE<span class="lead"></span><span class="item__price">18,00</span></div><p class="de">Ein Spieß aus Maishähnchenbrust-Stücken</p><p class="en">One skewer of corn chicken breast pieces</p></div>
      <div class="item"><div class="item__row">SHISHLIK<span class="lead"></span><span class="item__price">29,00</span></div><p class="de">Gegrillte Lammkarree-Stücke</p><p class="en">Grilled lamb chops</p></div>
    </div>
    <div class="col">
      <div class="item"><div class="item__row">BARG<span class="lead"></span><span class="item__price">23,00</span></div><p class="de">Ein Spieß aus flach geklopftem Lammrücken</p><p class="en">One skewer of lamb rack</p></div>
      <div class="item"><div class="item__row">CHENJE<span class="lead"></span><span class="item__price">23,00</span></div><p class="de">Ein Spieß aus Lammfilet-Stücken</p><p class="en">One skewer of lamb fillet pieces</p></div>
      <div class="item"><div class="item__row">DJUDJE SOLTANI<span class="lead"></span><span class="item__price">25,00</span></div><p class="de">Ein Spieß aus Maishähnchenbrust-Stücken und ein Lammhackfleisch-Spieß</p><p class="en">One skewer of corn chicken breast pieces and one of lamb minced meat</p></div>
    </div>
  </div>

  <h2 class="heading" style="left:52px;right:52px;top:198px"><span class="heading__rule"></span>Schmorgerichte<span class="heading__slash">//</span><span class="heading__en">braised dishes</span><span class="heading__rule"></span></h2>
  <div class="intro" style="top:217px"><p>Alle Schmorgerichte werden mit Safran verfeinertem Basmatireis Serviert<br><span class="en-line">All Braised Dishes are served with saffron rice</span></p></div>

  <div class="cols braised">
    <div class="col">
      <div class="item"><div class="item__row">BAMIEH<span class="lead"></span><span class="item__price">17,00</span></div><p class="de">Gericht mit Fleischstücken aus der Lammkeule und Okraschoten</p><p class="en">Sauce made from pieces of meat from leg of lamb and okras</p></div>
      <div class="item"><div class="item__row">BADEMJAN<span class="lead"></span><span class="item__price">16,00</span></div><p class="de">Gericht mit Fleischstücken aus der Lammkeule und Auberginen</p><p class="en">Sauce made from pieces of meat from leg of lamb and aubergines</p></div>
      <div class="item"><div class="item__row">FESENJAN<span class="lead"></span><span class="item__price">21,00</span></div><p class="de">Gericht aus geriebenen Walnüssen und Granatapfel Mark Wahlweise mit Lammhackbällchen, Maishähnchenbrust oder Maishähnchenkeule</p><p class="en">Sauce made from grated walnut and pomegranate sauce with lamb meatballs, corn chicken breast or corn chicken drumstick</p></div>
    </div>
    <div class="col">
      <div class="item"><div class="item__row">GHEIMEH BADEMJAN<span class="lead"></span><span class="item__price">17,00</span></div><p class="de">Gericht mit Fleischstücken aus der Lammkeule, Auberginen und Linsen</p><p class="en">Sauce made from pieces of meat from leg of lamb, aubergines and lentil</p></div>
      <div class="item"><div class="item__row">GHORME SABSI<span class="lead"></span><span class="item__price">16,00</span></div><p class="de">Gericht mit Fleischstücken aus der Lammkeule, Bohnen, Limette und verschiedenen Kräutern (Schnittlauch, Petersilie, Bockshornklee)</p><p class="en">Sauce made from pieces of meat from leg of lamb, beans, lemon and various herbs (Chives, parsley, fenugreek)</p></div>
    </div>
  </div>

  <h2 class="heading" style="left:52px;right:52px;top:354px"><span class="heading__rule"></span>Reisgerichte<span class="heading__slash">//</span><span class="heading__en">Rice dishes</span><span class="heading__rule"></span></h2>

  <div class="cols rice">
    <div class="col">
      <div class="item"><div class="item__row">BAGHALI POLO BA MAHICHE<span class="lead"></span><span class="item__price">22,00</span></div><p class="de">Geschmorte Lamm Haxe, serviert mit Basmatireis mit dicken Bohnen und Dillspitze, verfeinert mit Safran und Zimt</p><p class="en">Braised knuckle of lamb, served with basmati rice with beans, dill tips and cinnamon</p></div>
      <div class="item"><div class="item__row">SERESHK POLO BA MAHICHE<span class="lead"></span><span class="item__price">22,00</span></div><p class="de">Geschmorte Lamm Haxe, serviert mit Basmatireis mit gebratenen Berberitzen</p><p class="en">Braised knuckle of lamb, served with basmati rice with fried berberis</p></div>
      <div class="item"><div class="item__row">SHIRIN POLO BA MORGH<span class="lead"></span><span class="item__price">18,00</span></div><p class="de">Geschmorte Maishähnchenkeule, serviert mit Basmatireis mit Mandelsplittern, gehackten Pistazien, Orangenschale und Karotten</p><p class="en">Braised corn chicken drumstick, served with basmati rice with slivered almonds, chopped pistachios, orange peel and carrots</p></div>
    </div>
    <div class="col">
      <div class="item"><div class="item__row">BAGHALI POLO BA MORGH<span class="lead"></span><span class="item__price">18,00</span></div><p class="de">Geschmorte Maishähnchenkeule, serviert mit Basmatireis mit dicken Bohnen und Dillspitze, verfeinert mit Safran und Zimt</p><p class="en">Braised corn chicken drumstick, served with basmati rice with beans, dill tips and cinnamon</p></div>
      <div class="item"><div class="item__row">SERESHK POLO BA MORGH<span class="lead"></span><span class="item__price">18,00</span></div><p class="de">Geschmorte Maishähnchenkeule, serviert mit Basmatireis mit gebratenen Berberitzen</p><p class="en">Braised corn chicken drumstick, served with basmati rice with fried berberis</p></div>
    </div>
  </div>

  <p class="recommend">Wir empfehlen ihnen zu unseren Hauptgerichten Masto Muzir, Masto Khiar, Salat Shirazi oder unsere hausgemachte Chili Sauce<br><span class="en-line">We recommend Masto muzir, Masto khiar, Salad shirazi or our homemade chili sauce with all of our main dishes</span></p>
</section>

</body>
</html>
```